Making our lobbying activities and sports better visible for members and partners.

We are the Velden Assocation of Leisure Gear Merchant and and Trade. We are doing lobbying and having several special groupings and services. With a better power point we want to show better to the board, the members and partner what we are doing.

```html
<!DOCTYPE html>
<html lang="en">
<head>
<meta charset="utf-8">
<title>VALGMT – Presentation Overview</title>
<link rel="stylesheet" href="https://fonts.googleapis.com/css2?family=Montserrat:wght@400;500;600;700&display=swap">
<style>
:root{
  --sand:#e5d7ab;
  --navy:#2d2e3f;
  --blue:#18a5ee;
  --blue-deep:#1a9bea;
  --royal:#2b3dbd;
  --ink:#2d2e3f;
  --text:#5a5b66;
  --white:#ffffff;
  --grey:#eeeeee;
  --slate:#9aa0b5;
}
*{margin:0;padding:0;box-sizing:border-box}
html,body{width:1200px;height:1200px;overflow:hidden;background:var(--sand)}
body{font-family:'Montserrat',sans-serif;color:var(--ink)}
.board{position:absolute;left:0;top:0;width:1932px;height:1932px;transform:scale(0.62112);transform-origin:0 0}
.slide{position:absolute;width:432px;height:244px;background:var(--white);overflow:hidden}
.slide.dark{background:var(--navy)}
.abs{position:absolute}
.s-title{position:absolute;left:32px;top:14px;font-size:20px;font-weight:500;color:var(--ink);letter-spacing:.2px}
.dark .s-title{color:var(--white)}
.rule{position:absolute;left:20px;right:34px;top:228px;height:1px;background:var(--blue)}
.pg{position:absolute;right:19px;top:222px;width:10px;height:10px;background:var(--navy);color:#fff;font-size:4px;display:flex;align-items:center;justify-content:center}
.dark .pg{background:var(--blue)}
.mark{position:absolute;right:20px;top:17px;width:10px;height:10px;background:var(--navy)}
.dark .mark{background:var(--white)}
.lorem{font-size:5.6px;line-height:1.6;color:var(--text)}
.lorem b{color:var(--ink)}
.dark .lorem{color:#c9cad3}
.h-sm{font-size:9px;font-weight:500;color:var(--ink)}
.dark .h-sm{color:#fff}
.photo{position:absolute}
.stat{position:absolute;top:132px;width:86px;height:78px;color:#fff;text-align:center;padding-top:10px}
.stat strong{display:block;font-size:12px;font-weight:600;margin-bottom:8px}
.stat span{display:block;font-size:4.8px;line-height:1.7;padding:0 10px;color:#e6f3fc}
.box-out{position:absolute;width:113px;height:66px;border:1.5px solid var(--blue);padding:8px}
.btn{position:absolute;width:96px;height:22px;font-size:5px;display:flex;align-items:center;justify-content:center}
.bar{position:absolute;bottom:0}
</style>
</head>
<body>
<div class="board">

<!-- Row 1 -->
<section class="slide dark" style="left:68px;top:185px">
  <div class="abs" style="left:0;right:0;top:110px;display:flex;align-items:center;justify-content:center;gap:10px">
    <span style="width:14px;height:14px;background:var(--blue)"></span>
    <span style="font-size:36px;font-weight:600;color:#fff;letter-spacing:1px">VALGMT</span>
  </div>
</section>

<section class="slide" style="left:523px;top:185px">
  <h2 class="s-title">Agenda</h2>
  <div class="abs" style="left:330px;top:12px;width:58px;height:58px;background:var(--navy)"></div>
  <div class="abs" style="left:33px;top:95px;font-size:7px;font-weight:500;line-height:1">
    <p><span style="font-size:15px;color:var(--blue);margin-right:8px">01</span>Your Title Here</p>
    <p style="margin-top:18px"><span style="font-size:15px;margin-right:8px">02</span>Your Title Here</p>
    <p style="margin-top:16px"><span style="font-size:15px;color:var(--blue);margin-right:8px">03</span>Your Title Here</p>
  </div>
  <div class="abs" style="left:248px;top:95px;font-size:7px;font-weight:500;line-height:1">
    <p><span style="font-size:15px;color:var(--blue);margin-right:8px">04</span>Your Title Here</p>
    <p style="margin-top:18px"><span style="font-size:15px;margin-right:8px">05</span>Your Title Here</p>
    <p style="margin-top:16px"><span style="font-size:15px;color:var(--blue);margin-right:8px">06</span>Your Title Here</p>
  </div>
  <div class="rule"></div>
</section>

<section class="slide" style="left:978px;top:185px;background:var(--blue-deep)">
  <svg class="abs" width="432" height="244" style="left:0;top:0"><polygon points="30,0 160,0 110,244 0,244 0,90" fill="#25aef3"/></svg>
  <div class="abs" style="left:330px;top:12px;width:50px;height:50px;background:var(--navy)"></div>
  <h2 class="abs" style="left:0;right:0;top:98px;text-align:center;font-size:20px;font-weight:500;color:#fff">Mission</h2>
  <p class="abs lorem" style="left:58px;right:58px;top:128px;text-align:center;color:#fff"><b style="color:#fff">Lorem Ipsum</b> is simply dummy text of the printing and typesetting industry. Lorem Ipsum has been the industry's standard dummy text ever since the 1500s, when an unknown printer took a galley of type and scrambled it to make a type specimen book. It has survived not only five centuries.</p>
  <div class="rule" style="background:#bfe6fb"></div>
  <div class="pg">3</div>
</section>

<section class="slide" style="left:1432px;top:185px">
  <h2 class="s-title">Business Plan Concept</h2>
  <svg class="abs" width="432" height="244" style="left:0;top:0"><polygon points="310,0 410,0 380,72 278,72" fill="var(--royal)"/><polygon points="250,168 432,240 432,200 330,200" fill="var(--royal)"/><polygon points="360,200 432,200 432,244 400,244" fill="var(--royal)"/></svg>
  <div class="photo" role="img" aria-label="Photo of a tall historic building against a pale sky" style="left:252px;top:72px;width:180px;height:128px;background:linear-gradient(150deg,#dfe6ef 0%,#c8d3e0 55%,#b98a6a 100%)"></div>
  <p class="abs lorem" style="left:32px;top:80px;width:200px"><b>Lorem Ipsum</b> is simply dummy text of the printing and typesetting industry. Lorem Ipsum has been the industry's standard dummy text ever since the 1500s, when an unknown printer took a galley of type and scrambled it to make a type specimen book.</p>
  <p class="abs lorem" style="left:38px;top:132px;width:190px">✓ Lorem ipsum dolor sit amet,<br>&nbsp;&nbsp;&nbsp;consectetur adipiscing elit,<br>✓ sed do eiusmod tempor incididunt ut<br>&nbsp;&nbsp;&nbsp;labore et dolore magna</p>
  <div class="rule"></div>
  <div class="pg">4</div>
</section>

<!-- Row 2 -->
<section class="slide" style="left:68px;top:461px">
  <h2 class="s-title" style="left:42px">Profile</h2>
  <div class="mark"></div>
  <p class="abs lorem" style="left:42px;top:56px;width:198px;text-align:justify">Lorem ipsum dolor sit amet, consectetur adipiscing elit, sed do eiusmod tempor incididunt ut labore et dolore magna aliqua. Ut enim ad minim veniam, quis nostrud exercitation ullamco laboris nisi ut aliquip ex ea commodo consequat. Duis aute irure dolor in reprehenderit in</p>
  <div class="photo" role="img" aria-label="Photo of a person writing at a bright desk" style="left:250px;top:50px;width:154px;height:77px;background:linear-gradient(135deg,#eef1f3,#c9d2d8 60%,#a7b4bb)"></div>
  <div class="stat" style="left:40px;background:var(--navy)"><strong>500</strong><span>Lorem ipsum dolor sit amet, consectetur adipiscing elit, sed do eiusmod</span></div>
  <div class="stat" style="left:133px;background:var(--blue)"><strong>20+</strong><span>Lorem ipsum dolor sit amet, consectetur adipiscing elit, sed do eiusmod</span></div>
  <div class="stat" style="left:226px;background:var(--navy)"><strong>600</strong><span>Lorem ipsum dolor sit amet, consectetur adipiscing elit, sed do eiusmod</span></div>
  <div class="stat" style="left:318px;background:var(--blue)"><strong>5000</strong><span>Lorem ipsum dolor sit amet, consectetur adipiscing elit, sed do eiusmod</span></div>
  <div class="rule"></div>
  <div class="pg">5</div>
</section>

<section class="slide" style="left:523px;top:461px">
  <h2 class="s-title">Content Slide</h2>
  <div class="mark"></div>
  <div class="abs lorem" style="left:32px;top:66px;width:368px;font-size:5.2px;text-align:justify">
    <p><b>Lorem Ipsum</b> is simply dummy text of the printing and typesetting industry. Lorem Ipsum has been the industry's standard dummy text ever since the 1500s, when an unknown printer took a galley of type and scrambled it to make a type specimen book. It has survived not only five centuries, but also the leap into electronic typesetting, remaining essentially unchanged. It was popularised in the 1960s with the release of Typeleaf sheets containing Lorem Ipsum passages, and more recently with desktop publishing software like Pagewright Studio.</p>
    <p style="margin-top:6px"><b>Lorem Ipsum</b> is simply dummy text of the printing and typesetting industry. Lorem Ipsum has been the industry's standard dummy text ever since the 1500s, when an unknown printer took a galley of type and scrambled it to make a type specimen book. It has survived not only five centuries, but also the leap into electronic typesetting, remaining essentially unchanged. It was popularised in the 1960s with the release of Typeleaf sheets containing Lorem Ipsum.</p>
    <p style="margin-top:6px"><b>Lorem Ipsum</b> is simply dummy text of the printing and typesetting industry. Lorem Ipsum has been the industry's standard dummy text ever since the 1500s, when an unknown printer took a galley of type and scrambled it to make a type specimen book. It has survived not only five centuries, but also the leap into electronic typesetting, remaining essentially unchanged. It was popularised in the 1960s with the release of Typeleaf sheets.</p>
  </div>
  <div class="rule"></div>
  <div class="pg">6</div>
</section>

<section class="slide" style="left:978px;top:461px">
  <h2 class="s-title">Content Two Column</h2>
  <div class="mark"></div>
  <div class="abs lorem" style="left:32px;top:64px;width:168px;font-size:4.9px">
    <p><b>Lorem Ipsum</b> is simply dummy text of the printing and typesetting industry. Lorem Ipsum has been the industry's standard dummy text ever since the 1500s, when an unknown printer took a galley of type and scrambled it to make a type specimen book. It has survived not only five centuries, but also the leap into electronic typesetting, remaining essentially unchanged. It was popularised in the 1960s with the release of Typeleaf sheets containing Lorem Ipsum passages.</p>
    <p style="margin-top:6px"><b>Lorem Ipsum</b> is simply dummy text of the printing and typesetting industry. Lorem Ipsum has been the industry's standard dummy text ever since the 1500s, when an unknown printer took a galley of type and scrambled it to make a type specimen book. It has survived not only five centuries, but also the leap into electronic typesetting, remaining essentially unchanged. It was popularised in the 1960s.</p>
  </div>
  <div class="abs lorem" style="left:230px;top:64px;width:168px;font-size:4.9px">
    <p><b>Lorem Ipsum</b> is simply dummy text of the printing and typesetting industry. Lorem Ipsum has been the industry's standard dummy text ever since the 1500s, when an unknown printer took a galley of type and scrambled it to make a type specimen book. It has survived not only five centuries, but also the leap into electronic typesetting, remaining essentially unchanged. It was popularised in the 1960s with the release of Typeleaf sheets containing Lorem Ipsum passages.</p>
    <p style="margin-top:6px"><b>Lorem Ipsum</b> is simply dummy text of the printing and typesetting industry. Lorem Ipsum has been the industry's standard dummy text ever since the 1500s, when an unknown printer took a galley of type and scrambled it to make a type specimen book. It has survived not only five centuries, but also the leap into electronic typesetting, remaining essentially unchanged. It was popularised in the 1960s.</p>
  </div>
  <div class="rule"></div>
  <div class="pg">7</div>
</section>

<section class="slide" style="left:1432px;top:461px">
  <div class="photo" role="img" aria-label="Photo of a team joining hands in a high five over a desk" style="left:0;top:0;width:137px;height:244px;background:linear-gradient(160deg,#4b4640,#8a7a66 55%,#cfc6b8)"></div>
  <div class="photo" role="img" aria-label="Photo of cheering colleagues celebrating success" style="left:140px;top:0;width:132px;height:244px;background:linear-gradient(170deg,#c7cdd2,#8d949c 55%,#4c5460)"></div>
  <div class="mark"></div>
  <h2 class="abs" style="left:290px;top:46px;font-size:19px;font-weight:500;line-height:1.1">WHY WE<br><span style="color:var(--blue);font-weight:600">BEST</span></h2>
  <p class="abs h-sm" style="left:290px;top:110px">Your Title Here</p>
  <p class="abs lorem" style="left:290px;top:130px;width:120px">Lorem ipsum dolor sit amet, consectetur adipiscing elit, sed do eiusmod tempor incididunt ut labore et dolore magna aliqua. Ut enim ad minim veniam,</p>
  <div class="pg">8</div>
</section>

<!-- Row 3 -->
<section class="slide" style="left:68px;top:737px">
  <div class="abs" style="left:262px;top:16px;width:120px;height:120px;background:var(--navy)"></div>
  <h2 class="abs" style="left:20px;top:112px;font-size:34px;font-weight:600;color:var(--blue)">SECTION</h2>
  <p class="abs lorem" style="left:20px;top:160px;width:170px">Lorem ipsum dolor sit amet, consectetur adipiscing elit, sed do eiusmod tempor incididunt ut labore et dolore magna aliqua. Ut enim ad minim veniam,</p>
</section>

<section class="slide dark" style="left:523px;top:737px">
  <div class="abs" style="left:262px;top:16px;width:120px;height:120px;background:var(--white)"></div>
  <h2 class="abs" style="left:20px;top:112px;font-size:34px;font-weight:600;color:var(--blue)">SECTION</h2>
  <p class="abs lorem" style="left:20px;top:160px;width:170px">Lorem ipsum dolor sit amet, consectetur adipiscing elit, sed do eiusmod tempor incididunt ut labore et dolore magna aliqua. Ut enim ad minim veniam,</p>
</section>

<section class="slide dark" style="left:978px;top:737px">
  <h2 class="s-title">Heading</h2>
  <div class="mark" style="background:var(--white)"></div>
  <p class="abs" style="left:32px;top:74px;width:92px;font-size:11px;font-weight:500;color:#fff;line-height:1.18">Think ahead. Don't let day-to-day operations drive out planning.</p>
  <p class="abs lorem" style="left:32px;top:144px;width:92px;font-size:4.5px">Lorem Ipsum is simply dummy text of the printing and typesetting industry. Lorem Ipsum has been</p>
  <div class="abs" style="left:182px;top:68px;width:62px"><p class="h-sm" style="font-size:8px">Your Title</p><p class="lorem" style="font-size:4.3px;margin-top:4px">Lorem Ipsum is simply dummy text of the printing and typesetting industry. Lorem Ipsum has been</p></div>
  <div class="abs" style="left:300px;top:68px;width:62px"><p class="h-sm" style="font-size:8px">Your Title</p><p class="lorem" style="font-size:4.3px;margin-top:4px">Lorem Ipsum is simply dummy text of the printing and typesetting industry. Lorem Ipsum has been</p></div>
  <div class="abs" style="left:182px;top:141px;width:62px"><p class="h-sm" style="font-size:8px">Your Title</p><p class="lorem" style="font-size:4.3px;margin-top:4px">Lorem Ipsum is simply dummy text of the printing and typesetting industry. Lorem Ipsum has been</p></div>
  <div class="abs" style="left:300px;top:141px;width:62px"><p class="h-sm" style="font-size:8px">Your Title</p><p class="lorem" style="font-size:4.3px;margin-top:4px">Lorem Ipsum is simply dummy text of the printing and typesetting industry. Lorem Ipsum has been</p></div>
  <div class="rule"></div>
  <div class="pg">11</div>
</section>

<section class="slide" style="left:1432px;top:737px">
  <h2 class="s-title">Objectives</h2>
  <div class="mark"></div>
  <div class="abs" style="left:30px;top:52px;width:155px;height:163px;background:var(--blue);padding:12px 11px">
    <p style="font-size:15.5px;font-weight:500;color:#fff">WHY WE BEST</p>
    <p class="lorem" style="color:#fff;margin-top:8px;font-size:5.5px"><b style="color:#fff">Lorem Ipsum</b> is simply dummy text of the printing and typesetting industry. Lorem Ipsum has been the industry's standard dummy text ever since the 1500s, when an unknown printer took a galley of type and scrambled it to make a type specimen book. It has survived not only five centuries, but also the leap into electronic typesetting, remaining essentially unchanged. It was popularised in the</p>
  </div>
  <div class="abs" style="left:208px;top:50px;width:195px;height:78px;background:var(--navy);padding:12px 17px">
    <p class="h-sm" style="color:#fff">Your Title Here</p>
    <p class="lorem" style="margin-top:6px;color:#c9cad3">Lorem ipsum dolor sit amet, consectetur adipiscing elit, sed do eiusmod tempor incididunt ut labore et dolore magna aliqua. Ut enim ad minim veniam,</p>
  </div>
  <p class="abs h-sm" style="left:210px;top:157px">Your Title Here</p>
  <p class="abs lorem" style="left:210px;top:177px;width:196px">Lorem ipsum dolor sit amet, consectetur adipiscing elit, sed do eiusmod tempor incididunt ut labore et dolore magna aliqua. Ut enim ad minim veniam,</p>
  <div class="rule"></div>
  <div class="pg">12</div>
</section>

<!-- Row 4 -->
<section class="slide" style="left:68px;top:1013px">
  <h2 class="s-title">Heading</h2>
  <div class="mark"></div>
  <div class="abs" style="left:0;top:72px;width:113px;height:80px;background:var(--navy);text-align:center;padding-top:24px"><p class="h-sm" style="color:#fff;font-size:7px">Your Title</p><p class="lorem" style="color:#c9cad3;font-size:4.3px;margin-top:4px;padding:0 24px">Lorem ipsum dolor sit amet, consectetur</p></div>
  <div class="abs" style="left:113px;top:72px;width:108px;height:80px;background:var(--blue);text-align:center;padding-top:24px"><p class="h-sm" style="color:#fff;font-size:7px">Your Title</p><p class="lorem" style="color:#fff;font-size:4.3px;margin-top:4px;padding:0 22px">Lorem ipsum dolor sit amet, consectetur</p></div>
  <div class="abs" style="left:221px;top:72px;width:111px;height:80px;background:var(--navy);text-align:center;padding-top:24px"><p class="h-sm" style="color:#fff;font-size:7px">Your Title</p><p class="lorem" style="color:#c9cad3;font-size:4.3px;margin-top:4px;padding:0 24px">Lorem ipsum dolor sit amet, consectetur</p></div>
  <div class="photo" role="img" aria-label="Aerial photo of a road winding through an autumn forest" style="left:332px;top:72px;width:100px;height:172px;background:linear-gradient(160deg,#6f7b3c,#b48a2e 45%,#5c6a38 80%,#3f4a2c)"></div>
  <p class="abs lorem" style="left:32px;top:170px;width:290px;font-size:4.5px"><b>Lorem Ipsum</b> is simply dummy text of the printing and typesetting industry. Lorem Ipsum has been the industry's standard dummy text ever since the 1500s, when an unknown printer took a galley of type and scrambled it to make a type specimen book. It has survived not only five centuries, <b>Lorem Ipsum</b> is simply dummy text of the printing and typesetting industry. Lorem Ipsum has been the industry's standard dummy text ever since the 1500s, when an unknown printer took a galley of type and scrambled it to make a type specimen book. It has survived not only five centuries.</p>
  <div class="pg" style="background:var(--blue)">13</div>
</section>

<section class="slide" style="left:523px;top:1013px">
  <div class="abs" style="left:0;top:0;width:432px;height:137px;background:var(--navy)"></div>
  <div class="mark" style="background:var(--white)"></div>
  <h2 class="abs" style="left:32px;top:40px;font-size:20px;font-weight:500;color:#fff">Services</h2>
  <p class="abs lorem" style="left:32px;top:72px;width:372px;color:#c9cad3;font-size:5.2px">Lorem ipsum dolor sit amet, consectetur adipiscing elit, sed do eiusmod tempor incididunt ut labore et dolore magna aliqua. Ut enim ad minim veniam, quis nostrud exercitation ullamco laboris nisi ut aliquip ex ea commodo consequat. Duis aute irure dolor in reprehenderit in voluptate velit esse cillum dolore eu fugia Lorem ipsum dolor sit amet, consectetur adipiscing elit, sed do eiusmod tempor incididunt ut labore et dolore magna aliqua. Ut enim ad minim veniam, quis nostrud exercitation ullamco laboris nisi ut aliquip ex ea commodo consequat. Duis aute irure dolor in reprehenderit in voluptate velit esse cillum dolore eu fugia</p>
  <div class="abs" style="left:32px;top:160px;width:110px"><p class="h-sm">Your Title Here</p><p class="lorem" style="margin-top:5px">Lorem ipsum dolor sit amet, consectetur adipiscing elit, sed do eiusmod tempor incididunt ut labore et dolore</p></div>
  <div class="abs" style="left:156px;top:160px;width:110px"><p class="h-sm">Your Title Here</p><p class="lorem" style="margin-top:5px">Lorem ipsum dolor sit amet, consectetur adipiscing elit, sed do eiusmod tempor incididunt ut labore et dolore</p></div>
  <div class="abs" style="left:300px;top:160px;width:104px"><p class="h-sm">Your Title Here</p><p class="lorem" style="margin-top:5px">Lorem ipsum dolor sit amet, consectetur adipiscing elit, sed do eiusmod tempor incididunt ut labore et dolore</p></div>
  <div class="rule"></div>
  <div class="pg">14</div>
</section>

<section class="slide" style="left:978px;top:1013px">
  <h2 class="s-title">SERVICS</h2>
  <div class="mark"></div>
  <div class="box-out" style="left:30px;top:56px"><p class="h-sm" style="font-size:8px">Your Title</p><p class="lorem" style="font-size:4.3px;margin-top:4px">Lorem Ipsum is simply dummy text of the printing and typesetting industry. Lorem Ipsum has been</p></div>
  <div class="box-out" style="left:159px;top:56px"><p class="h-sm" style="font-size:8px">Your Title</p><p class="lorem" style="font-size:4.3px;margin-top:4px">Lorem Ipsum is simply dummy text of the printing and typesetting industry. Lorem Ipsum has been</p></div>
  <div class="box-out" style="left:290px;top:56px"><p class="h-sm" style="font-size:8px">Your Title</p><p class="lorem" style="font-size:4.3px;margin-top:4px">Lorem Ipsum is simply dummy text of the printing and typesetting industry. Lorem Ipsum has been</p></div>
  <div class="box-out" style="left:30px;top:139px"><p class="h-sm" style="font-size:8px">Your Title</p><p class="lorem" style="font-size:4.3px;margin-top:4px">Lorem Ipsum is simply dummy text of the printing and typesetting industry. Lorem Ipsum has been</p></div>
  <div class="box-out" style="left:159px;top:139px"><p class="h-sm" style="font-size:8px">Your Title</p><p class="lorem" style="font-size:4.3px;margin-top:4px">Lorem Ipsum is simply dummy text of the printing and typesetting industry. Lorem Ipsum has been</p></div>
  <div class="box-out" style="left:290px;top:139px"><p class="h-sm" style="font-size:8px">Your Title</p><p class="lorem" style="font-size:4.3px;margin-top:4px">Lorem Ipsum is simply dummy text of the printing and typesetting industry. Lorem Ipsum has been</p></div>
  <div class="rule"></div>
  <div class="pg">15</div>
</section>

<section class="slide" style="left:1432px;top:1013px">
  <h2 class="s-title">Title</h2>
  <div class="mark"></div>
  <div class="photo" role="img" aria-label="Photo of a ferris wheel against a blue sky" style="left:0;top:57px;width:157px;height:154px;background:linear-gradient(180deg,#6f93b4,#a9bfd3 60%,#d6dde4)"></div>
  <p class="abs" style="left:198px;top:60px;width:190px;font-size:7px;font-weight:600;line-height:1.2">Lorem Ipsum is simply dummy text of the printing and typesetting industry. Lorem Ipsum has been the</p>
  <div class="abs" style="left:201px;top:96px;width:90px"><p class="h-sm" style="color:var(--royal);font-size:8px">Your Title Here</p><p class="lorem" style="font-size:4.5px;margin-top:3px">Lorem ipsum dolor sit amet, consectetur adipiscing elit, sed do eiusmod tempor incididunt ut</p></div>
  <div class="abs" style="left:318px;top:96px;width:90px"><p class="h-sm" style="color:var(--royal);font-size:8px">Your Title Here</p><p class="lorem" style="font-size:4.5px;margin-top:3px">Lorem ipsum dolor sit amet, consectetur adipiscing elit, sed do eiusmod tempor incididunt</p></div>
  <div class="abs" style="left:201px;top:169px;width:90px"><p class="h-sm" style="color:var(--royal);font-size:8px">Your Title Here</p><p class="lorem" style="font-size:4.5px;margin-top:3px">Lorem ipsum dolor sit amet, consectetur adipiscing elit, sed do eiusmod tempor incididunt ut</p></div>
  <div class="abs" style="left:318px;top:169px;width:90px"><p class="h-sm" style="color:var(--royal);font-size:8px">Your Title Here</p><p class="lorem" style="font-size:4.5px;margin-top:3px">Lorem ipsum dolor sit amet, consectetur adipiscing elit, sed do eiusmod tempor incididunt</p></div>
  <div class="rule"></div>
  <div class="pg">16</div>
</section>

<!-- Row 5 -->
<section class="slide" style="left:68px;top:1289px">
  <h2 class="s-title">Detail Slide</h2>
  <div class="mark"></div>
  <p class="abs lorem" style="left:32px;top:58px;width:176px;font-size:5.3px"><b>Lorem Ipsum</b> is simply dummy text of the printing and typesetting industry. Lorem Ipsum has been the industry's standard dummy text ever since the 1500s, when an unknown printer took a galley of type and scrambled it to make a type specimen book. It has survived not only five centuries, but also the leap into electronic typesetting, remaining essentially unchanged. It was popularised in the 1960s with the release of Typeleaf sheets containing Lorem Ipsum passages.<br><b>Lorem Ipsum</b> is simply dummy text of the printing and typesetting industry. Lorem Ipsum has been the industry's standard dummy text ever since the 1500s, when an unknown printer took a galley of type and scrambled it to make a type specimen book. It has survived not only five centuries.</p>
  <div class="abs" style="left:222px;top:58px;width:184px;height:140px;background:var(--navy);padding:13px 11px;box-shadow:1px 2px 3px rgba(0,0,0,.15)"><p style="font-size:18px;font-weight:500;color:#fff;line-height:1.05">Business Plan<br>Deckmaker</p></div>
  <div class="rule"></div>
  <div class="pg">17</div>
</section>

<section class="slide" style="left:523px;top:1289px">
  <h2 class="s-title">Services with Image</h2>
  <div class="mark"></div>
  <div class="abs" style="left:0;top:67px;width:113px;height:87px;background:var(--blue);padding:20px 18px"><p class="h-sm" style="color:#fff;font-size:7px;line-height:1.1">Your Title<br>Here</p><p class="lorem" style="color:#fff;font-size:4.5px;margin-top:2px">Lorem ipsum dolor sit amet, consectetur adipiscing elit, sed do eiusmod tempor incididunt</p></div>
  <div class="abs" style="left:0;top:154px;width:113px;height:90px;background:var(--navy);padding:20px 18px"><p class="h-sm" style="color:#fff;font-size:7px;line-height:1.1">Your Title<br>Here</p><p class="lorem" style="color:#c9cad3;font-size:4.5px;margin-top:2px">Lorem ipsum dolor sit amet, consectetur adipiscing elit, sed do eiusmod tempor incididunt</p></div>
  <div class="abs" style="left:113px;top:67px;width:90px;height:177px;background:var(--grey)"></div>
  <p class="abs lorem" style="left:217px;top:74px;width:188px">Lorem ipsum dolor sit amet, consectetur adipiscing elit, sed do eiusmod tempor incididunt ut labore et dolore magna aliqua. Ut enim ad minim veniam, quis nostrud exercitation ullamco laboris nisi ut aliquip ex ea commodo consequat.</p>
  <div class="abs" style="left:228px;top:141px;width:80px"><p class="h-sm" style="font-size:7px">Your Title Here</p><p class="lorem" style="font-size:4.5px">Lorem ipsum dolor sit amet, consectetur</p></div>
  <div class="abs" style="left:325px;top:141px;width:80px"><p class="h-sm" style="font-size:7px">Your Title Here</p><p class="lorem" style="font-size:4.5px">Lorem ipsum dolor sit amet, consectetur</p></div>
  <div class="abs" style="left:228px;top:190px;width:80px"><p class="h-sm" style="font-size:7px">Your Title Here</p><p class="lorem" style="font-size:4.5px">Lorem ipsum dolor sit amet, consectetur</p></div>
  <div class="abs" style="left:325px;top:190px;width:80px"><p class="h-sm" style="font-size:7px">Your Title Here</p><p class="lorem" style="font-size:4.5px">Lorem ipsum dolor sit amet, consectetur</p></div>
  <div class="rule" style="left:203px"></div>
  <div class="pg">18</div>
</section>

<section class="slide" style="left:978px;top:1289px">
  <p class="abs" style="left:36px;top:32px;width:170px;font-size:10.5px;font-weight:500;line-height:1.2">Think ahead. Don't let day-to-day operations drive out planning.</p>
  <p class="abs lorem" style="left:36px;top:92px;width:164px;font-size:4.8px;line-height:2.2">Lorem ipsum dolor sit amet, consectetur adipiscing elit, sed do eiusmod tempor incididunt ut labore et dolore magna aliqua. Ut enim ad minim veniam, quis nostrud exercitation ullamco laboris nisi ut aliquip ex ea commodo consequat. Duis aute irure dolor in reprehenderit in voluptate velit esse cillum dolore eu fugiat nulla pariatur. Excepteur sint occaecat cupidatat non proident, sunt in culpa qui officia deserunt mollit anim id est</p>
  <div class="photo" role="img" aria-label="Photo of a wooden desk with newspapers, a laptop and coffee" style="left:230px;top:0;width:202px;height:160px;background:linear-gradient(135deg,#d9d6cf,#9b8066 45%,#6b4f3a 75%,#c8c4bb)"></div>
  <div class="abs" style="left:230px;top:160px;width:202px;height:84px;background:var(--navy);padding:12px 12px"><p style="font-size:11px;font-weight:500;color:#fff">Your Title Here</p><p class="lorem" style="color:#c9cad3;font-size:5px;margin-top:3px">Lorem ipsum dolor sit amet, consectetur adipiscing elit, sed do eiusmod tempor incididunt</p></div>
  <div class="rule" style="right:34px"></div>
  <div class="pg" style="background:var(--blue)">19</div>
</section>

<section class="slide" style="left:1432px;top:1289px">
  <h2 class="abs" style="left:32px;top:22px;font-size:18px;font-weight:500;line-height:1.1">More<br>Content</h2>
  <p class="abs" style="left:32px;top:138px;width:90px;font-size:10px;font-weight:500;line-height:1.15">Think ahead. Don't let day-to-day operations drive out planning.</p>
  <div class="abs" style="left:158px;top:0;width:110px;height:244px;background:var(--navy)"></div>
  <svg class="abs" width="110" height="244" style="left:158px;top:0" fill="none" stroke="#fff" stroke-width="1">
    <rect x="48" y="34" width="13" height="13"/><path d="M51 37h7v7h-7z"/>
    <path d="M54 96a6 6 0 1 1 2 0v5h-2z"/><path d="M53 104h4"/>
    <path d="M45 160h5v12h-5z M50 170l2 2h9l2-7h-7l1-5-2-1-5 6"/>
  </svg>
  <p class="abs lorem" style="left:168px;top:54px;width:90px;text-align:center;color:#fff;font-size:4.2px;line-height:1.2">Lorem ipsum dolor sit amet</p>
  <p class="abs lorem" style="left:168px;top:113px;width:90px;text-align:center;color:#fff;font-size:4.2px;line-height:1.2">Lorem ipsum dolor sit amet</p>
  <p class="abs lorem" style="left:168px;top:178px;width:90px;text-align:center;color:#fff;font-size:4.2px;line-height:1.2">Lorem ipsum dolor sit amet</p>
  <div class="mark"></div>
  <p class="abs lorem" style="left:294px;top:62px;width:116px;font-size:4.6px;line-height:2.35">Lorem ipsum dolor sit amet, consectetur adipiscing elit, sed do eiusmod tempor incididunt ut labore et dolore magna aliqua. Ut enim ad minim veniam, quis nostrud exercitation ullamco laboris nisi ut aliquip ex ea commodo consequat. Duis aute irure dolor in reprehenderit in voluptate velit esse cillum dolore eu fugiat nulla pariatur. Excepteur sint occaecat cupidatat non proident, sunt in culpa qui officia deserunt mollit anim id est</p>
  <div class="rule" style="left:268px"></div>
  <div class="pg">20</div>
</section>

<!-- Row 6 -->
<section class="slide" style="left:68px;top:1565px">
  <h2 class="s-title">Title</h2>
  <div class="mark"></div>
  <div class="abs" style="left:0;top:64px;width:168px;height:102px;background:var(--blue);padding:8px 0 0 18px"><p style="font-size:17.5px;font-weight:500;color:#fff;line-height:1.1">Free<br>Business<br>Plan<br>Deckmaker</p></div>
  <div class="btn" style="left:188px;top:64px;border:1.5px solid var(--blue);color:var(--ink);box-shadow:1px 1px 3px rgba(0,0,0,.2)">Goals are Completed</div>
  <div class="btn" style="left:304px;top:62px;background:var(--blue);color:#fff;box-shadow:1px 1px 3px rgba(0,0,0,.2)">Goals are Completed</div>
  <p class="abs lorem" style="left:190px;top:92px;width:96px">Lorem ipsum dolor sit amet, consectetur adipiscing elit, sed do eiusmod tempor</p>
  <p class="abs lorem" style="left:306px;top:90px;width:96px">Lorem ipsum dolor sit amet, consectetur adipiscing elit, sed do eiusmod tempor</p>
  <div class="btn" style="left:188px;top:144px;background:#4c5266;color:#fff;box-shadow:1px 1px 3px rgba(0,0,0,.2)">Goals are Completed</div>
  <div class="btn" style="left:304px;top:142px;background:var(--navy);color:#fff;box-shadow:1px 1px 3px rgba(0,0,0,.2)">Goals are Completed</div>
  <p class="abs lorem" style="left:190px;top:172px;width:96px">Lorem ipsum dolor sit amet, consectetur adipiscing elit, sed do eiusmod tempor</p>
  <p class="abs lorem" style="left:306px;top:170px;width:96px">Lorem ipsum dolor sit amet, consectetur adipiscing elit, sed do eiusmod tempor</p>
  <div class="rule"></div>
  <div class="pg">21</div>
</section>

<section class="slide" style="left:523px;top:1565px">
  <h2 class="s-title">Numbers Points</h2>
  <div class="mark"></div>
  <div class="abs" style="left:30px;top:60px;width:127px;height:162px;background:var(--royal);padding:10px 9px">
    <p style="font-size:7.5px;font-weight:500;color:#fff;line-height:1.25">IN THE BUSINESS<br>WORLD,</p>
  </div>
  <div class="abs" style="left:44px;top:112px;width:100px;height:94px">
    <div class="bar" style="left:0;width:9px;height:74px;background:#fff"></div><div class="bar" style="left:0;width:9px;height:42px;background:var(--slate)"></div>
    <div class="bar" style="left:26px;width:9px;height:78px;background:#fff"></div><div class="bar" style="left:26px;width:9px;height:26px;background:var(--slate)"></div>
    <div class="bar" style="left:52px;width:9px;height:62px;background:#fff"></div><div class="bar" style="left:52px;width:9px;height:36px;background:var(--slate)"></div>
    <div class="bar" style="left:78px;width:9px;height:86px;background:#fff"></div><div class="bar" style="left:78px;width:9px;height:44px;background:var(--slate)"></div>
  </div>
  <div class="abs" style="left:172px;top:62px;width:218px;height:30px;background:var(--grey);border-radius:3px"></div>
  <div class="abs" style="left:172px;top:138px;width:218px;height:30px;background:var(--grey);border-radius:3px"></div>
  <div class="abs" style="left:185px;top:68px;width:200px">
    <p style="display:flex;gap:10px;align-items:center;height:20px"><span style="font-size:11px;font-weight:600">01</span><span class="lorem" style="font-size:4.6px">Lorem ipsum dolor sit amet, consectetur adipiscing elit, sed do eiusmod tempor incididunt ut labore et dolore magna aliqua</span></p>
    <p style="display:flex;gap:10px;align-items:center;height:20px;margin-top:18px"><span style="font-size:11px;font-weight:600">02</span><span class="lorem" style="font-size:4.6px">Lorem ipsum dolor sit amet, consectetur adipiscing elit, sed do eiusmod tempor incididunt ut labore et dolore magna aliqua</span></p>
    <p style="display:flex;gap:10px;align-items:center;height:20px;margin-top:18px"><span style="font-size:11px;font-weight:600">03</span><span class="lorem" style="font-size:4.6px">Lorem ipsum dolor sit amet, consectetur adipiscing elit, sed do eiusmod tempor incididunt ut labore et dolore magna aliqua</span></p>
    <p style="display:flex;gap:10px;align-items:center;height:20px;margin-top:17px"><span style="font-size:11px;font-weight:600">04</span><span class="lorem" style="font-size:4.6px">Lorem ipsum dolor sit amet, consectetur adipiscing elit, sed do eiusmod tempor incididunt ut labore et dolore magna aliqua</span></p>
  </div>
  <div class="rule"></div>
  <div class="pg">22</div>
</section>

<section class="slide" style="left:978px;top:1565px">
  <h2 class="s-title">Graph Data</h2>
  <div class="mark"></div>
  <svg class="abs" width="432" height="150" style="left:0;top:56px">
    <g><rect x="44" y="7" width="22" height="62" fill="var(--royal)"/><rect x="66" y="34" width="22" height="35" fill="#8e93ad"/><rect x="88" y="43" width="22" height="26" fill="#b6bccd"/><line x1="26" y1="69" x2="130" y2="69" stroke="#ccc" stroke-width=".8"/></g>
    <g><rect x="180" y="7" width="22" height="62" fill="var(--royal)"/><rect x="202" y="34" width="22" height="35" fill="#8e93ad"/><rect x="224" y="43" width="22" height="26" fill="#b6bccd"/><line x1="162" y1="69" x2="266" y2="69" stroke="#ccc" stroke-width=".8"/></g>
    <g><rect x="306" y="7" width="22" height="62" fill="var(--royal)"/><rect x="328" y="34" width="22" height="35" fill="#8e93ad"/><rect x="350" y="43" width="22" height="26" fill="#b6bccd"/><line x1="288" y1="69" x2="392" y2="69" stroke="#ccc" stroke-width=".8"/></g>
    <g font-family="Montserrat,sans-serif" font-size="3.6" fill="#777" text-anchor="middle"><text x="78" y="76">January</text><text x="214" y="76">January</text><text x="340" y="76">January</text></g>
  </svg>
  <div class="abs" style="left:34px;top:176px;width:104px"><p class="h-sm" style="font-size:8px">Your Title Here</p><p class="lorem" style="font-size:4.6px">Lorem ipsum dolor sit amet, consectetur adipiscing elit, sed do</p></div>
  <div class="abs" style="left:172px;top:176px;width:104px"><p class="h-sm" style="font-size:8px">Your Title Here</p><p class="lorem" style="font-size:4.6px">Lorem ipsum dolor sit amet, consectetur adipiscing elit, sed do</p></div>
  <div class="abs" style="left:310px;top:176px;width:104px"><p class="h-sm" style="font-size:8px">Your Title Here</p><p class="lorem" style="font-size:4.6px">Lorem ipsum dolor sit amet, consectetur adipiscing elit, sed do</p></div>
  <div class="rule"></div>
  <div class="pg">23</div>
</section>

<section class="slide" style="left:1432px;top:1565px">
  <h2 class="abs" style="left:40px;top:78px;width:210px;text-align:center;font-size:46px;font-weight:600;line-height:1.0;letter-spacing:1px">THANK<br>YOU</h2>
  <div class="abs" style="left:296px;top:74px;width:84px;height:84px;background:var(--navy)"></div>
</section>

</div>
</body>
</html>
```